Not Your Average Diet Book Cover Design

I need a book cover designed for a project titled:
Title: Table Route Junction
Sub-title: The Hidden Key To Gently Mastering Your Meals
Author: Carla Brightwood
Designation: Not a Doctor
The book is a look at 8 trendy diets (Atkins, Whole Foods, Paleo, Keto, Mediterranean, Sugar Free, Alkaline and Intermittent Fasting), with each chapter covering the pros and cons of one.
The theme throughout the book is that, when approached as a diet, they are each doomed to failure. When sustainability and lifestyle are taken into consideration, however, any one of them (or a combination of two or more) can lead to overall health and weight management.
Vegetables, mindset and habit creation are 3 of the "overlap" factors implied in the title.
I have uploaded a temporary cover that I am using as a placeholder at the moment. I do NOT want anything like it. (Use the tagline above, not the one in the sample cover).
Please, NO images of scales, stomachs, or anything else that is super cliche for the weight loss industry.
This is a full length book, written in a conversation tone, that I want to stand out from the a) copy and pasted online "experts" and b) doctors and fitpros who think it's their way or the highway. I want it to be welcoming and accessible.
I want the book to appeal to an audience who is currently struggling with their health and most likely failed at many diets in the past.
I will need a print cover for a 6"x 9" Pressbloom book, as well as a Lumora cover and an Sonvera cover.
I would like all source files, including any fonts used. For delivery, placeholder text can be used for the back cover.
Target Market(s)
Male & Female
Overweight
Unhealthy, but not severely so
Have tried diets before and failed
Age: 25-55 (average)
Income: $30-50k USD
Marital status: Single OR not entirely satisfied with the relationship
Location: Canada, USA, Australia, UK
Industry/Entity Type
Health And Wellness
Colors
Designer to choose colors to be used in the design.
Requirements
Must have
- Title: Table Route Junction
- Sub-title: The Hidden Key To Gently Mastering Your Meals
- Author: Carla Brightwood
- Designation: Not a Doctor
Nice to have
- A welcoming, understanding feeling
- Implications of holistic health
Should not have
- Images:
- - Scale or measuring tapes, etc
- - stomachs/abs
- - yoga or any silhouettes
- A look similar to the sample.

```html
<!DOCTYPE html>
<html lang="en">
<head>
<meta charset="utf-8">
<title>Table Route Junction – Cover Spread</title>
<link href="https://fonts.googleapis.com/css2?family=Gilda+Display&family=Montserrat:wght@600&family=Quicksand:wght@400;700&family=Tinos&display=swap" rel="stylesheet">
<style>
  :root {
    --page: #ffffff;
    --canvas: #ffffff;
    --shade: #e4e4e4;
    --ink: #1c1c1c;
    --ink-soft: #2b2b2b;
    --rule: #222222;
    --sun: #f6d35a;
    --tan: #c9a15e;
    --peach: #f3b48c;
    --lime: #c9d15a;
    --rose: #d8728f;
  }
  * { margin: 0; padding: 0; box-sizing: border-box; }
  html, body { width: 1200px; height: 1200px; overflow: hidden; background: var(--canvas); }
  .canvas { position: relative; width: 1200px; height: 1200px; }
  .spread {
    position: absolute; left: 50px; top: 199px; width: 1100px; height: 803px;
    display: flex; box-shadow: 0 10px 40px rgba(0,0,0,0.10);
  }
  .back-cover {
    position: relative; width: 500px; height: 100%;
    background: linear-gradient(90deg, var(--page) 55%, var(--shade) 100%);
  }
  .back-title {
    position: absolute; left: 43px; top: 44px;
    font: 600 17px/1 "Montserrat", sans-serif; color: var(--ink);
  }
  .back-copy {
    position: absolute; left: 43px; width: 440px;
    font: 16.5px/24.5px "Tinos", serif; color: var(--ink-soft);
  }
  .back-copy.intro { top: 104px; }
  .back-copy.about { top: 304px; }
  .back-copy .author-name { font-family: "Quicksand", sans-serif; font-size: 18px; }
  .colour-band {
    position: absolute; left: 51px; top: 505px; width: 435px; height: 95px;
    border-radius: 48px; opacity: 0.6;
    background: linear-gradient(90deg, var(--sun), var(--tan) 25%, var(--peach) 50%, var(--lime) 72%, var(--rose));
  }
  .barcode-frame {
    position: absolute; left: 272px; top: 654px; width: 206px; height: 103px;
    border: 2px solid var(--rule); background: linear-gradient(90deg, #fff, #f0f0f0);
  }
  .spine {
    position: relative; width: 92px; height: 100%;
    background: linear-gradient(90deg, #f4f4f4, #ffffff 40%, #e9e9e9);
  }
  .spine-title, .spine-author {
    position: absolute; left: 50%; writing-mode: vertical-rl; transform: translateX(-50%);
    white-space: nowrap; color: var(--ink);
  }
  .spine-title { top: 42px; font: 27px/1 "Gilda Display", serif; }
  .spine-author { top: 506px; font: 400 16px/1 "Quicksand", sans-serif; }
  .spine-author b { font-weight: 700; }
  .front-cover {
    position: relative; width: 508px; height: 100%; text-align: center;
    background: linear-gradient(90deg, var(--shade) 0%, var(--page) 40%);
  }
  .front-title {
    position: absolute; left: 0; right: 0; top: 44px;
    font: 62px/80px "Gilda Display", serif; color: var(--ink);
  }
  .front-subtitle {
    position: absolute; left: 0; right: 0; top: 208px;
    font: 400 16px/1 "Quicksand", sans-serif; color: var(--ink);
  }
  .food-wheel {
    position: absolute; left: 50px; top: 268px; width: 410px; height: 420px; border-radius: 50%;
    background: radial-gradient(circle, #f1e6ee 0%, #f3efe2 35%, #eef0dc 55%, rgba(255,255,255,0) 72%),
                conic-gradient(from 200deg, #e9c3b0, #cdd59c, #e6d3a4, #f0d27a, #d9a9b6, #e8b2a0, #e9c3b0);
    opacity: 0.85;
  }
  .front-author {
    position: absolute; left: 0; right: 0; top: 715px;
    font: 700 16px/21px "Quicksand", sans-serif; color: var(--ink);
  }
  .front-author span { display: block; font-weight: 400; }
</style>
</head>
<body>
<div class="canvas">
  <div class="spread">
    <section class="back-cover">
      <h2 class="back-title">TABLE ROUTE JUNCTION</h2>
      <p class="back-copy intro">Lorem ipsum dolor sit amet, consectetuer adipiscing elit, sed diam nonummy nibh euismod tincidunt ut laoreet dolore magna aliquam erat volutpat. Ut wisi enim ad minim veniam, quis nostrud exerci tation ullamcorper suscipit lobortis nisl ut aliquip ex ea commodo consequat. Duis autem vel eum iriure</p>
      <p class="back-copy about"><span class="author-name">Carla Brightwood</span> dolor sit amet, consectetuer adipiscing elit, sed diam nonummy nibh euismod tincidunt ut laoreet dolore magna aliquam erat volutpat. Ut wisi enim ad minim veniam, quis nostrud exerci tation ullamcorper suscipit lobortis nisl ut aliquip ex ea commodo consequat.</p>
      <div class="colour-band" role="img" aria-label="Decorative row of soft overlapping colour dots in yellow, tan, peach, lime and rose"></div>
      <div class="barcode-frame"></div>
    </section>
    <section class="spine">
      <div class="spine-title">Table Route Junction</div>
      <div class="spine-author"><b>Carla Brightwood</b> Not a Doctor</div>
    </section>
    <section class="front-cover">
      <h1 class="front-title">Table Route<br>Junction</h1>
      <p class="front-subtitle">The Hidden Key To Gently Mastering Your Meals</p>
      <div class="food-wheel" role="img" aria-label="Ring of overlapping coloured circles holding food photos — avocado, cauliflower, olive oil, grains, toast, meat, eggs and beans — around a pastel brain"></div>
      <p class="front-author">Carla Brightwood<span>Not a Doctor</span></p>
    </section>
  </div>
</div>
</body>
</html>
```